Tolvek Consulting
Tolvek Consulting stationary
Tolvek Consulting - Consulting
Creative Brief
Professional
Daniel R. Tolvek
Chief Executive Officer
Tolvek Consulting, LLC P.O. Box 4372 Phoenix, AZ 85004
daniel@danielrtolvek-mail.com
danielrtolvek-mail.com
Tolvek Consulting Logo

```html
<!DOCTYPE html>
<html lang="en">
<head>
<meta charset="utf-8">
<title>Tolvek Consulting – Business Cards</title>
<link href="https://fonts.googleapis.com/css2?family=Arimo:wght@400;700&display=swap" rel="stylesheet">
<style>
  :root {
    --bg: #e9e6e1;
    --card-light: #ffffff;
    --card-light-edge: #e4e6ea;
    --card-dark: #1a1a1c;
    --card-dark-edge: #050506;
    --brand-blue: #1c86cf;
    --brand-orange: #f07a1a;
    --ink-dark: #222326;
    --ink-mid: #55585e;
    --ink-light: #d8d9dc;
    --ink-light-soft: #a9abb0;
  }
  * { box-sizing: border-box; margin: 0; padding: 0; }
  html, body { width: 1200px; height: 911px; overflow: hidden; }
  body {
    background: var(--bg);
    font-family: "Arimo", Arial, sans-serif;
    position: relative;
  }
  .card {
    position: absolute;
    width: 500px;
    height: 286px;
    border-radius: 14px;
    overflow: hidden;
    box-shadow: 0 10px 24px rgba(0,0,0,.22);
  }
  .card--light { background: linear-gradient(135deg, var(--card-light) 45%, var(--card-light-edge)); }
  .card--dark { background: linear-gradient(135deg, #2a2a2d 0%, var(--card-dark) 40%, var(--card-dark-edge)); }
  .card--front-light { left: 80px; top: 150px; }
  .card--front-dark { left: 620px; top: 150px; }
  .card--back-light { left: 80px; top: 480px; }
  .card--back-dark { left: 620px; top: 480px; }

  .deco-circle {
    position: absolute;
    right: -40px; top: 20px;
    width: 260px; height: 260px;
    border-radius: 50%;
  }
  .card--light .deco-circle { background: radial-gradient(circle, rgba(28,134,207,.08), rgba(240,122,26,.06) 60%, transparent 72%); }
  .card--dark .deco-circle { background: radial-gradient(circle, rgba(28,134,207,.14), rgba(240,122,26,.08) 60%, transparent 72%); }

  .brand {
    position: absolute;
    display: flex; align-items: center; gap: 12px;
  }
  .brand__mark {
    width: 34px; height: 34px;
    background: var(--brand-orange);
    border-radius: 4px;
  }
  .brand__name {
    font-weight: 700;
    font-size: 25px;
    letter-spacing: 1px;
    line-height: 1.05;
    color: var(--brand-blue);
    text-transform: uppercase;
  }
  .card--front-light .brand, .card--front-dark .brand { left: 36px; top: 36px; }

  .contact { position: absolute; left: 36px; top: 128px; }
  .contact__name { font-weight: 700; font-size: 19px; }
  .contact__title { font-size: 11px; margin-top: 3px; }
  .contact__company { font-size: 11.5px; margin-top: 14px; line-height: 1.4; }
  .contact__list { list-style: none; margin-top: 4px; font-size: 11.5px; line-height: 1.55; }
  .contact__list li { display: flex; align-items: center; gap: 7px; }
  .contact__list svg { width: 10px; height: 10px; flex: none; }

  .card--light .contact__name { color: var(--ink-dark); }
  .card--light .contact__title, .card--light .contact__company, .card--light .contact__list { color: var(--ink-mid); }
  .card--dark .contact__name { color: var(--ink-light); }
  .card--dark .contact__title, .card--dark .contact__company, .card--dark .contact__list { color: var(--ink-light-soft); }

  .back-mark {
    position: absolute; right: 40px; top: 120px;
    width: 48px; height: 48px;
    background: var(--brand-orange);
    border-radius: 6px;
  }
  .back-url {
    position: absolute; right: 36px; bottom: 30px;
    font-size: 12px;
  }
  .card--light .back-url { color: var(--ink-mid); }
  .card--dark .back-url { color: var(--ink-light); }
</style>
</head>
<body>

  <section class="card card--light card--front-light">
    <div class="deco-circle"></div>
    <div class="brand">
      <span class="brand__mark"></span>
      <span class="brand__name">Tolvek<br>Consulting</span>
    </div>
    <div class="contact">
      <p class="contact__name">Daniel R. Tolvek</p>
      <p class="contact__title">Chief Executive Officer</p>
      <p class="contact__company">Tolvek Consulting, LLC<br>P.O. Box 4372 Phoenix, AZ 85004</p>
      <ul class="contact__list">
        <li><svg viewBox="0 0 10 10"><path d="M2 1h2l1 2-1 1a5 5 0 0 0 2 2l1-1 2 1v2l-1 1C4 9 1 6 1 2z" fill="currentColor"/></svg>480.555.0172</li>
        <li><svg viewBox="0 0 10 10"><rect x="1" y="2" width="8" height="6" fill="none" stroke="currentColor"/><path d="M1 2l4 3 4-3" fill="none" stroke="currentColor"/></svg>daniel@danielrtolvek-mail.com</li>
        <li><svg viewBox="0 0 10 10"><circle cx="5" cy="5" r="4" fill="none" stroke="currentColor"/><path d="M1 5h8M5 1v8" stroke="currentColor"/></svg>www.danielrtolvek-mail.com</li>
      </ul>
    </div>
  </section>

  <section class="card card--dark card--front-dark">
    <div class="deco-circle"></div>
    <div class="brand">
      <span class="brand__mark"></span>
      <span class="brand__name">Tolvek<br>Consulting</span>
    </div>
    <div class="contact">
      <p class="contact__name">Daniel R. Tolvek</p>
      <p class="contact__title">Chief Executive Officer</p>
      <p class="contact__company">Tolvek Consulting, LLC<br>P.O. Box 4372 Phoenix, AZ 85004</p>
      <ul class="contact__list">
        <li><svg viewBox="0 0 10 10"><path d="M2 1h2l1 2-1 1a5 5 0 0 0 2 2l1-1 2 1v2l-1 1C4 9 1 6 1 2z" fill="currentColor"/></svg>480.555.0172</li>
        <li><svg viewBox="0 0 10 10"><rect x="1" y="2" width="8" height="6" fill="none" stroke="currentColor"/><path d="M1 2l4 3 4-3" fill="none" stroke="currentColor"/></svg>daniel@danielrtolvek-mail.com</li>
        <li><svg viewBox="0 0 10 10"><circle cx="5" cy="5" r="4" fill="none" stroke="currentColor"/><path d="M1 5h8M5 1v8" stroke="currentColor"/></svg>www.danielrtolvek-mail.com</li>
      </ul>
    </div>
  </section>

  <section class="card card--light card--back-light">
    <div class="deco-circle"></div>
    <span class="back-mark"></span>
    <p class="back-url">www.danielrtolvek-mail.com</p>
  </section>

  <section class="card card--dark card--back-dark">
    <div class="deco-circle"></div>
    <span class="back-mark"></span>
    <p class="back-url">www.danielrtolvek-mail.com</p>
  </section>

</body>
</html>
```